New Website for consulting company

We need a completely new design for our company web site: www.morvane-partners.ch (please do not use it as a reference. We want something completely different.)
We are a consulting company and therefore our team is our key ressource together with our skills.
This site will be german in the first place. It will be the webmasters job to create it multilingual.
The website should be rather eccentric but still informative.
For colors and logo please refer to attached Logodefinition.pdf. The colored horizontal logo should be somehow used for the website but doesn't need to be extremely prominent. You can choose every color for the design but the logo must be somehow embedded in original colors and the green should be integrated for the site.
Please keep in mind that it should also work for mobile devices so the webmaster will have to create a responsive website out of the submitted design.
The main Page should be a one pager with different layout blocks directly accessible via top sticky menubar.:
- AKTEURE (team), gallery, people centric with images of member and expandable description box, plus skills abstract list (name & description). See attached mockups to support the explaining (do not take it as a reference).
- ÜBER UNS (mission), Description of companies vision, mission, competences etc.
- ... according to the menu bar
We would like to have at least 3 different block layouts to fill with content for the one pager site:
1. Team is the most important and the least generic one
2. Big picture less text
3. Multiple smaller pictures multiple text blocks
4. Hardly any picture text centric
The page should communicate competence in what we are doing, quality and not least youth and freshness.
See Attachements:
- Logodefinition.pdf: Logo definition containing definition of color of the logo.
- mockup_Website_mock1.png: These should give you an impression of how it is meant to have layouted blocks

```html
<!DOCTYPE html>
<html lang="en">
<head>
<meta charset="utf-8">
<title>Morvane Partners</title>
<link href="https://fonts.googleapis.com/css2?family=Open+Sans:wght@300;400;600;700&display=swap" rel="stylesheet">
<style>
:root{
  --green:#5cb531;
  --green-dark:#4a9a25;
  --ink:#333333;
  --muted:#8a8a8a;
  --dark:#2b2b2b;
  --darker:#222222;
  --light:#efefef;
  --white:#ffffff;
}
*{box-sizing:border-box;margin:0;padding:0}
html,body{width:1200px;height:5279px;overflow:hidden}
body{font-family:"Open Sans",Arial,sans-serif;color:var(--ink);background:var(--white);font-size:12px;line-height:1.6}
section,header,footer{position:relative;width:1200px;overflow:hidden}
.wrap{width:1004px;margin:0 auto;position:relative}
.title{font-weight:300;text-align:center;font-size:40px;letter-spacing:1px;line-height:1.2}
.title.green{color:var(--green)}
p{color:var(--muted)}

/* hero */
.hero{height:605px;background:linear-gradient(100deg,#b9c6b7 0%,#d8dfd6 30%,#9eaaa6 55%,#c9b6a4 75%,#e7e2dc 100%)}
.hero-photo{position:absolute;inset:0}
.brand{position:absolute;left:488px;top:20px;width:224px;height:118px;background:var(--green);display:flex;align-items:center;gap:12px;padding:0 16px;border:3px solid var(--white)}
.brand-mark{width:70px;height:70px;background:var(--white);flex:none}
.brand-name{color:var(--white);font-weight:600;font-size:20px;line-height:1.2}
.hero-arrow{position:absolute;top:290px;width:24px;height:24px}
.hero-arrow.left{left:24px}.hero-arrow.right{right:24px}

/* nav */
.nav{height:57px;background:var(--white)}
.nav ul{list-style:none;display:flex;width:1004px;margin:0 auto;height:57px;background:var(--green);align-items:center;justify-content:space-between;padding:0 10px}
.nav li{color:var(--white);font-size:12px;font-weight:600;padding:12px 18px}
.nav li.active{background:var(--white);color:var(--green);border:1px solid var(--green)}

/* welcome */
.welcome{height:658px;padding-top:72px;text-align:center}
.welcome .lead{width:880px;margin:22px auto 0;font-size:12px}
.welcome h3{font-weight:400;font-size:20px;margin-top:30px;color:var(--ink)}
.welcome .strong{color:var(--ink);font-size:14px;margin-top:10px}
.news{width:1004px;margin:34px auto 0;height:150px;background:var(--dark);display:flex;align-items:center;padding:0 24px;gap:24px;text-align:left}
.news-date{background:var(--darker);color:var(--white);width:70px;height:100px;text-align:center;padding-top:10px;line-height:1.15}
.news-date b{display:block;font-size:34px}
.news p{color:#bdbdbd;font-size:11px}
.news .more{color:var(--white);font-size:10px;font-weight:700;margin-top:8px}

/* jobs */
.jobs{height:650px;background:var(--light);padding-top:68px}
.job-grid{display:grid;grid-template-columns:repeat(4,218px);gap:42px 28px;width:960px;margin:50px auto 0}
.job{background:var(--white);height:204px;padding:14px 16px}
.job-brand{font-weight:700;font-size:17px;color:var(--ink);height:34px}
.job h4{font-size:12px;font-weight:700;line-height:1.4;margin-top:6px}
.job p{font-size:10px;margin-top:8px;line-height:1.5}
.btn{display:inline-block;background:var(--green);color:var(--white);font-size:10px;font-weight:600;padding:5px 12px;margin-top:14px}

/* competencies */
.comp{height:670px;padding-top:100px}
.comp .intro{width:1004px;margin:26px auto 0;text-align:center;font-size:11px}
.comp-grid{display:grid;grid-template-columns:repeat(3,320px);gap:70px 32px;width:1004px;margin:60px auto 0}
.comp-item{display:flex;gap:16px}
.icon{width:60px;height:60px;background:var(--green);flex:none;display:flex;align-items:center;justify-content:center}
.comp-item h4{font-size:16px;font-weight:600;color:var(--ink)}
.comp-item p{font-size:10px;line-height:1.5;margin-top:6px}

/* team */
.team-top{height:360px;background:var(--green);padding-top:68px}
.team-top .title{color:var(--white)}
.people{display:flex;justify-content:space-between;width:1004px;margin:28px auto 0}
.person{width:118px}
.portrait{height:132px;background:linear-gradient(180deg,#d9d9d9,#9c9c9c)}
.tag{background:var(--white);padding:8px 10px;height:50px;line-height:1.35}
.tag b{font-size:11px;display:block;font-weight:600}
.tag span{font-size:9px;color:var(--muted)}
.person.active .tag{background:var(--dark)}
.person.active .tag b{color:var(--white)}
.team-detail{height:336px;background:var(--dark);display:flex;padding:40px 98px 0;gap:30px}
.team-detail .bio{width:480px;font-size:11px;color:#b5b5b5}
.team-detail .bio p{color:#b5b5b5;margin-bottom:12px}
.skills{width:264px;list-style:none}
.skills li{background:var(--white);font-size:10px;padding:7px 10px;margin-bottom:8px;color:var(--ink)}
.detail-photo{width:196px;height:250px;background:linear-gradient(180deg,#cfcfcf,#7f7f7f)}
.pointer{position:absolute;left:348px;top:0;width:0;height:0;border-left:14px solid transparent;border-right:14px solid transparent;border-top:14px solid var(--green)}
.team-bottom{height:289px;background:var(--green);padding-top:36px}
.team-bottom .people{margin-top:0}

/* customers */
.customers{height:650px;padding-top:74px;text-align:center}
.customers h3{font-weight:400;font-size:15px;margin-top:12px}
.customers .intro{width:860px;margin:8px auto 0;font-size:11px}
.cust-grid{display:grid;grid-template-columns:repeat(4,236px);gap:20px;width:1004px;margin:26px auto 0;text-align:left}
.cust-img{height:170px}
.cust-grid h5{font-size:11px;font-weight:700;margin-top:14px}
.cust-grid p{font-size:10px;line-height:1.5;margin-top:4px}
.btn-outline{display:inline-block;border:1px solid var(--green);color:var(--green);font-size:12px;padding:14px 30px;margin-top:30px}

/* network */
.network{height:405px;background:var(--light);padding-top:58px}
.net-cols{display:flex;gap:60px;width:1004px;margin:0 auto}
.net-col{width:472px}
.net-col h2{font-weight:300;font-size:40px;line-height:1.1}
.net-col p{font-size:11px;margin-top:20px}
.ticks{list-style:none;margin-top:20px}
.ticks li{display:flex;align-items:center;gap:10px;font-size:11px;margin-bottom:14px}
.biz-row{display:flex;justify-content:space-between;align-items:flex-start}
.partner-badge{font-weight:700;font-size:22px;color:var(--ink);display:flex;align-items:center;gap:8px;margin-top:40px;margin-right:60px}
.partner-badge i{width:16px;height:16px;background:var(--green);display:block}

/* contact */
.contact{height:440px;background:linear-gradient(135deg,#6f6a62,#4f4c47 50%,#67625a)}
.contact-map{position:absolute;inset:0}
.boxes{position:absolute;left:310px;top:52px;display:flex;gap:24px}
.box{background:var(--white);width:280px;height:334px;padding:22px}
.box h3{font-weight:600;font-size:24px;line-height:1.1;border-bottom:1px solid #ddd;padding-bottom:12px}
.info{list-style:none;margin-top:22px}
.info li{display:flex;gap:12px;align-items:center;font-size:10px;margin-bottom:22px;line-height:1.4}
.info .ic{width:28px;height:28px;border-radius:50%;background:var(--dark);flex:none;display:flex;align-items:center;justify-content:center}
.field{border:1px solid #ddd;height:26px;margin-top:10px;font-size:10px;color:var(--muted);padding:5px 8px}
.field.tall{height:70px}
.submit{display:inline-block;background:var(--dark);color:var(--white);font-size:10px;padding:5px 12px;margin-top:12px}

/* footer */
.footer{height:159px;background:var(--darker);text-align:center;padding-top:40px}
.footer nav{color:#cfcfcf;font-size:11px;display:flex;justify-content:center;gap:12px}
.footer small{display:block;color:#8f8f8f;font-size:10px;margin-top:8px}
.social{display:flex;justify-content:center;gap:8px;margin-top:16px}
.social i{width:26px;height:26px;border-radius:50%;background:var(--white);display:block}
</style>
</head>
<body>

<header class="hero">
  <div class="hero-photo" role="img" aria-label="Photo of a smiling young businesswoman in front of blurred colleagues in a bright office"></div>
  <div class="brand"><div class="brand-mark"></div><div class="brand-name">Morvane<br>Partners</div></div>
  <svg class="hero-arrow left" viewBox="0 0 24 24"><path d="M15 4 7 12l8 8" fill="none" stroke="#fff" stroke-width="2"/></svg>
  <svg class="hero-arrow right" viewBox="0 0 24 24"><path d="M9 4l8 8-8 8" fill="none" stroke="#fff" stroke-width="2"/></svg>
</header>

<nav class="nav">
  <ul><li class="active">HOME</li><li>JOBS</li><li>COMPETENCIES</li><li>TEAM</li><li>CUSTOMERS</li><li>NETWORK</li><li>BUSINESS</li><li>CONTACT</li></ul>
</nav>

<section class="welcome">
  <h1 class="title green">WELCOME TO MORVANE PARTNERS</h1>
  <p class="lead">The challenges of our customers are marked by ever increasing quality demands by increasingly rapid change cycles. This is due to market conditions, of legal regulations or of financial conditions. These challenges can only usually be overcome by the use of computer science means. A purely technical consideration may prove fatal to the business. What is needed is a holistic, networked view of the problems and their possible solutions, taking into account strategic, organizational, economic and technical aspects: the only way to achieve an optimal solution.</p>
  <h3>Your success is our motivation.</h3>
  <p class="lead">We think and act holistically and networked, methodical and structured. To get to best Practices oriented, perfectly matched to your needs solutions, and so we continue to probe need and join their customers, we provide a regular facilitation in the form of consistent training.</p>
  <p class="lead" style="margin-top:10px">We are pleased to support you in your new projects.</p>
  <p class="strong">Profound knowledge and independently</p>
  <div class="news">
    <div class="news-date">JUN<b>13</b>2015</div>
    <div>
      <p>Donec vestibulum odio diam, at laoreet massa ullamcorper id. Donec molestie nisl et tellus hendrerit ultricies. Nunc eu ligula sed quam pulvinar maximus in vitae eros. Proin porta fermentum ipsum, vel porttitor lorem venenatis luctus. Vivamus volutpat ex sapien sed tempus, blandit feugiat massa finibus ac sagittis. Donec sit amet lacus non est semper laoreet ac nec nunc. Duis et auctor sapien.</p>
      <div class="more">READ MORE</div>
    </div>
  </div>
</section>

<section class="jobs">
  <h2 class="title">JOBS</h2>
  <div class="job-grid">
    <article class="job"><div class="job-brand">Fernlow</div><h4>Nulla porta libero nec mauris viverra imperdiet.</h4><p>Fusce auctor blandit orci gravida, ac pulvinar. Donec posuere nibh nisi arcu pellentesque, ut venenatis luctus.</p><span class="btn">Apply Now</span></article>
    <article class="job"><div class="job-brand">Quorix</div><h4>Nulla porta libero nec mauris viverra imperdiet.</h4><p>Fusce auctor blandit orci gravida, ac pulvinar. Donec posuere nibh nisi arcu pellentesque, ut venenatis luctus.</p><span class="btn">Apply Now</span></article>
    <article class="job"><div class="job-brand">Talvent</div><h4>Nulla porta libero nec mauris viverra imperdiet.</h4><p>Fusce auctor blandit orci gravida, ac pulvinar. Donec posuere nibh nisi arcu pellentesque, ut venenatis luctus.</p><span class="btn">Apply Now</span></article>
    <article class="job"><div class="job-brand">Brevik</div><h4>Nulla porta libero nec mauris viverra imperdiet.</h4><p>Fusce auctor blandit orci gravida, ac pulvinar. Donec posuere nibh nisi arcu pellentesque, ut venenatis luctus.</p><span class="btn">Apply Now</span></article>
    <article class="job"><div class="job-brand">Oskarel</div><h4>Nulla porta libero nec mauris viverra imperdiet.</h4><p>Fusce auctor blandit orci gravida, ac pulvinar. Donec posuere nibh nisi arcu pellentesque, ut venenatis luctus.</p><span class="btn">Apply Now</span></article>
    <article class="job"><div class="job-brand">Nyrate</div><h4>Nulla porta libero nec mauris viverra imperdiet.</h4><p>Fusce auctor blandit orci gravida, ac pulvinar. Donec posuere nibh nisi arcu pellentesque, ut venenatis luctus.</p><span class="btn">Apply Now</span></article>
    <article class="job"><div class="job-brand">Calbridge</div><h4>Nulla porta libero nec mauris viverra imperdiet.</h4><p>Fusce auctor blandit orci gravida, ac pulvinar. Donec posuere nibh nisi arcu pellentesque, ut venenatis luctus.</p><span class="btn">Apply Now</span></article>
    <article class="job"><div class="job-brand">Vantrel</div><h4>Nulla porta libero nec mauris viverra imperdiet.</h4><p>Fusce auctor blandit orci gravida, ac pulvinar. Donec posuere nibh nisi arcu pellentesque, ut venenatis luctus.</p><span class="btn">Apply Now</span></article>
  </div>
</section>

<section class="comp">
  <h2 class="title green">COMPETENCIES</h2>
  <p class="intro">For us, competence means combined with our experience to use our applied knowledge. With our skills for the holistic conception, management and implementation of changes at the interface between business and IT, we support our customers in strategic projects. The professional design leads to strategy, process and system level are needed here as well, such as the so-called "soft" aspects of change management. Inform yourself: About our services in the areas of business engineering and project management.</p>
  <div class="comp-grid">
    <div class="comp-item"><div class="icon"><svg width="30" height="30" viewBox="0 0 30 30"><rect x="4" y="4" width="22" height="22" fill="none" stroke="#fff" stroke-width="2.5"/><path d="M9 15l4 4 8-9" fill="none" stroke="#fff" stroke-width="2.5"/></svg></div><div><h4>Project Management</h4><p>Fusce auctor blandit orci gravida auctor. Donec posuere nibh nisi arcu pellentesque, ut venenatis.</p></div></div>
    <div class="comp-item"><div class="icon"><svg width="30" height="30" viewBox="0 0 30 30"><rect x="4" y="10" width="22" height="15" fill="#fff"/><rect x="11" y="5" width="8" height="6" fill="none" stroke="#fff" stroke-width="2.5"/></svg></div><div><h4>Business Engineering</h4><p>Fusce auctor blandit orci gravida auctor. Donec posuere nibh nisi arcu pellentesque, ut venenatis.</p></div></div>
    <div class="comp-item"><div class="icon"><svg width="30" height="30" viewBox="0 0 30 30"><path d="M7 3h12l5 5v19H7z" fill="#fff"/><path d="M11 14h10M11 19h10" stroke="#5cb531" stroke-width="2"/></svg></div><div><h4>ECM / GEVER</h4><p>Fusce auctor blandit orci gravida auctor. Donec posuere nibh nisi arcu pellentesque, ut venenatis.</p></div></div>
    <div class="comp-item"><div class="icon"><svg width="30" height="30" viewBox="0 0 30 30"><circle cx="11" cy="12" r="6" fill="none" stroke="#fff" stroke-width="3"/><circle cx="21" cy="21" r="4" fill="none" stroke="#fff" stroke-width="3"/></svg></div><div><h4>Process Management</h4><p>Fusce auctor blandit orci gravida auctor. Donec posuere nibh nisi arcu pellentesque, ut venenatis.</p></div></div>
    <div class="comp-item"><div class="icon"><svg width="30" height="30" viewBox="0 0 30 30"><path d="M6 25V14h5v11M13 25V8h5v17M20 25V4h5v21" fill="#fff"/></svg></div><div><h4>Strategy Consulting</h4><p>Fusce auctor blandit orci gravida auctor. Donec posuere nibh nisi arcu pellentesque, ut venenatis.</p></div></div>
    <div class="comp-item"><div class="icon"><svg width="30" height="30" viewBox="0 0 30 30"><rect x="3" y="5" width="24" height="16" fill="none" stroke="#fff" stroke-width="2.5"/><path d="M10 26h10M15 21v5" stroke="#fff" stroke-width="2.5"/></svg></div><div><h4>System Development</h4><p>Fusce auctor blandit orci gravida auctor. Donec posuere nibh nisi arcu pellentesque, ut venenatis.</p></div></div>
  </div>
</section>

<section class="team-top">
  <h2 class="title">TEAM</h2>
  <div class="people">
    <div class="person"><div class="portrait" role="img" aria-label="Portrait of a team member"></div><div class="tag"><b>Lukas Brenner</b><span>Project manager</span></div></div>
    <div class="person"><div class="portrait" role="img" aria-label="Portrait of a team member"></div><div class="tag"><b>Lukas Brenner</b><span>Project manager</span></div></div>
    <div class="person active"><div class="portrait" role="img" aria-label="Portrait of a team member"></div><div class="tag"><b>Lukas Brenner</b><span>Project manager</span></div></div>
    <div class="person"><div class="portrait" role="img" aria-label="Portrait of a team member"></div><div class="tag"><b>Lukas Brenner</b><span>Project manager</span></div></div>
    <div class="person"><div class="portrait" role="img" aria-label="Portrait of a team member"></div><div class="tag"><b>Lukas Brenner</b><span>Project manager</span></div></div>
    <div class="person"><div class="portrait" role="img" aria-label="Portrait of a team member"></div><div class="tag"><b>Lukas Brenner</b><span>Project manager</span></div></div>
    <div class="person"><div class="portrait" role="img" aria-label="Portrait of a team member"></div><div class="tag"><b>Lukas Brenner</b><span>Project manager</span></div></div>
  </div>
</section>

<section class="team-detail">
  <div class="pointer"></div>
  <div class="bio">
    <p>Praesent ut lobortis urna, in pulvinar erat. Pellentesque malesuada non urna eget egestas. Suspendisse sit enim vulputate arcu tempor hendrerit interdum ac nisl. Suspendisse condimentum vehicula massa at mollis nulla interdum maximus. Donec sed quam consectetur, venenatis felis et, pellentesque dui. Donec volutpat rutrum lorem vel ultricies. Pellentesque nibh libero, scelerisque nec lectus blandit, rhoncus eget ante.</p>
    <p>Proin non ante nunc. Vivamus in ipsum ipsum. Suspendisse potenti. Pellentesque venenatis, neque quis lobortis tempor, mi erat egestas justo, sit amet dictum ipsum lacus ut libero. Nulla vitae justo id nisi mollis in auctor sed. Vestibulum tincidunt eget nibh egestas porttitor. Ut congue hendrerit porta. Nullam vel arcu tellus laoreet fringilla. Curabitur tristique magna id dui ultrices commodo. Aenean vel bibendum lectus, ac pharetra eros.</p>
  </div>
  <ul class="skills">
    <li>Nullam sed posuere neque</li><li>Aliquam vulputate</li><li>Proin sollicitudin sed eget</li><li>Nulla vitae justo id nisi</li><li>Fusce commodo mauris nec odio</li><li>Donec posuere</li>
  </ul>
  <div class="detail-photo" role="img" aria-label="Larger portrait of the selected team member in a suit"></div>
</section>

<section class="team-bottom">
  <div class="people">
    <div class="person"><div class="portrait" role="img" aria-label="Portrait of a team member"></div><div class="tag"><b>Lukas Brenner</b><span>Project manager</span></div></div>
    <div class="person"><div class="portrait" role="img" aria-label="Portrait of a team member"></div><div class="tag"><b>Lukas Brenner</b><span>Project manager</span></div></div>
    <div class="person"><div class="portrait" role="img" aria-label="Portrait of a team member"></div><div class="tag"><b>Lukas Brenner</b><span>Project manager</span></div></div>
    <div class="person"><div class="portrait" role="img" aria-label="Portrait of a team member"></div><div class="tag"><b>Lukas Brenner</b><span>Project manager</span></div></div>
    <div class="person"><div class="portrait" role="img" aria-label="Portrait of a team member"></div><div class="tag"><b>Lukas Brenner</b><span>Project manager</span></div></div>
    <div class="person"><div class="portrait" role="img" aria-label="Portrait of a team member"></div><div class="tag"><b>Lukas Brenner</b><span>Project manager</span></div></div>
    <div class="person"><div class="portrait" role="img" aria-label="Portrait of a team member"></div><div class="tag"><b>Lukas Brenner</b><span>Project manager</span></div></div>
  </div>
</section>

<section class="customers">
  <h2 class="title green">CUSTOMERS</h2>
  <h3>Successful projects - satisfied customers</h3>
  <p class="intro">Through dedication, professionalism and reliability, we create trust and satisfaction of our customers. This creates permanent, genuine partnerships. We are happy to talk to you personally about our successes or provide upon request the direct contact with our customers here.</p>
  <div class="cust-grid">
    <div><div class="cust-img" role="img" aria-label="Photo of a smiling service agent with a headset" style="background:linear-gradient(135deg,#e9e4de,#c7bdb3)"></div><h5>SERVICE</h5><p>Donec sed quam consectetur, venenatis felis et, pellentesque dui. Donec volutpat rutrum lorem vel ultricies.</p></div>
    <div><div class="cust-img" role="img" aria-label="Photo of a government building with columns" style="background:linear-gradient(135deg,#8fb4d6,#d6dde3)"></div><h5>GOVERNMENT</h5><p>Donec sed quam consectetur, venenatis felis et, pellentesque dui. Donec volutpat rutrum lorem vel ultricies.</p></div>
    <div><div class="cust-img" role="img" aria-label="Photo of a telecommunication tower at dusk" style="background:linear-gradient(135deg,#3c4f8c,#c07a6a)"></div><h5>TELECOM &amp; IT</h5><p>Donec sed quam consectetur, venenatis felis et, pellentesque dui. Donec volutpat rutrum lorem vel ultricies.</p></div>
    <div><div class="cust-img" role="img" aria-label="Photo of a truck on a highway under a sunset sky" style="background:linear-gradient(135deg,#4b5d8a,#d79a7c)"></div><h5>TRANSPORTATION &amp; LOGISTICS</h5><p>Donec sed quam consectetur, venenatis felis et, pellentesque dui. Donec volutpat rutrum lorem vel ultricies.</p></div>
  </div>
  <span class="btn-outline">CONTACT US</span>
</section>

<section class="network">
  <div class="net-cols">
    <div class="net-col">
      <h2>NETWORK</h2>
      <p>Morvane Partners collaborates with other companies and organizations. Our extensive network allows us to employ the person for each project, which has the appropriate knowledge and the necessary experience. After all, success and motivation are closely related.</p>
      <ul class="ticks">
        <li><svg width="12" height="12" viewBox="0 0 12 12"><path d="M1 6l3 3 7-7" fill="none" stroke="#333" stroke-width="2"/></svg>Memberships</li>
        <li><svg width="12" height="12" viewBox="0 0 12 12"><path d="M1 6l3 3 7-7" fill="none" stroke="#333" stroke-width="2"/></svg>Partnerships</li>
        <li><svg width="12" height="12" viewBox="0 0 12 12"><path d="M1 6l3 3 7-7" fill="none" stroke="#333" stroke-width="2"/></svg>Sponsoring</li>
      </ul>
    </div>
    <div class="net-col">
      <h2>BUSINESS</h2>
      <p>Morvane Partners AG is a partnership, national service company. The company was founded in 2008 as a limited company and converted into a public limited company in May 2014. Founder and Managing Director is Reto Albrecht.</p>
      <div class="biz-row">
        <ul class="ticks">
          <li><svg width="12" height="12" viewBox="0 0 12 12"><path d="M1 6l3 3 7-7" fill="none" stroke="#333" stroke-width="2"/></svg>Jobs</li>
          <li><svg width="12" height="12" viewBox="0 0 12 12"><path d="M1 6l3 3 7-7" fill="none" stroke="#333" stroke-width="2"/></svg>Contact</li>
          <li><svg width="12" height="12" viewBox="0 0 12 12"><path d="M1 6l3 3 7-7" fill="none" stroke="#333" stroke-width="2"/></svg>Imprint</li>
          <li><svg width="12" height="12" viewBox="0 0 12 12"><path d="M1 6l3 3 7-7" fill="none" stroke="#333" stroke-width="2"/></svg>Signatures</li>
        </ul>
        <div class="partner-badge">LINKARA<i></i></div>
      </div>
    </div>
  </div>
</section>

<section class="contact">
  <div class="contact-map" role="img" aria-label="Dark street map of the office surroundings"></div>
  <div class="boxes">
    <div class="box">
      <h3>CONTACT US</h3>
      <ul class="info">
        <li><span class="ic"><svg width="12" height="14" viewBox="0 0 12 14"><path d="M6 13S1 7.5 1 5a5 5 0 0 1 10 0c0 2.5-5 8-5 8z" fill="#fff"/></svg></span>Seefeldstrasse 42<br>8008 Zürich</li>
        <li><span class="ic"><svg width="14" height="14" viewBox="0 0 14 14"><path d="M3 1l3 3-2 2a8 8 0 0 0 4 4l2-2 3 3-2 2C6 13 1 8 1 3z" fill="#fff"/></svg></span>044 555 18 40</li>
        <li><span class="ic"><svg width="14" height="14" viewBox="0 0 14 14"><rect x="2" y="5" width="10" height="7" fill="#fff"/><rect x="4" y="1" width="6" height="4" fill="#fff"/></svg></span>044 555 18 41</li>
        <li><span class="ic"><svg width="14" height="12" viewBox="0 0 14 12"><rect x="1" y="2" width="12" height="8" fill="#fff"/><path d="M1 2l6 5 6-5" fill="none" stroke="#2b2b2b"/></svg></span>info@morvane-partners.ch<br>www.morvane-partners.ch</li>
      </ul>
    </div>
    <div class="box">
      <h3>QUICK CONTACT</h3>
      <div class="field" style="margin-top:18px">Name</div>
      <div class="field">E-Mail</div>
      <div class="field">Phone</div>
      <div class="field tall">Message</div>
      <span class="submit">SUBMIT</span>
    </div>
  </div>
</section>

<footer class="footer">
  <nav><span>Home</span><span>Jobs</span><span>Competencies</span><span>Team</span><span>Customers</span><span>Network</span><span>Business</span><span>Contact</span></nav>
  <small>Copyright © 2015 Morvane Partners - All rights reserved.</small>
  <div class="social"><i></i><i></i><i></i><i></i><i></i><i></i><i></i></div>
</footer>

</body>
</html>
```